依頼詳細
12月1日の開催である為、クリスマスをイメージした上品なデザインで、配色はゴールドや赤色を希望しています。ターゲットは50代~70代のハイクラスな女性です。

記載項目
添付資料の通り、ご記載下さいませ。
サイズ
A4
ページ数
片面
希望イメージ
シンプル 複雑
単色 カラフル
暗い 明るい
日常 高級
遊び心 厳粛
未来的 伝統的
女性的 男性的
希望する色
赤系、ゴールドを思わせる色調を希望。
納品ファイル
• 高解像度JPG (.jpg)
• イラストレーター形式 (.ai)
補足説明
【チラシを御考案下さる皆様へ】

いつも素敵なデザインをご提案下さいまして、誠にありがとうございます。
この度は、第6回目となります「ひだまりチェロ・フェスティバルin岡山」のチラシデザインをお願いしたいと存じます。
出演者の皆様は、1分15秒のステージに向けて一生懸命に練習をされていますので、このチラシで出演者様もご来場者様もワクワクしていただけますと幸いに存じます。
どうぞ宜しくお願い申し上げます。

by.日本ひだまりチェロ連盟
追記:添付ファイルをご参照下さいませ。
大変素敵な御提案を下さり、誠にありがとうございます。
既に数点、感謝しつつ拝見しております。

背景についてですが、
必ずしもグランドピアノが必要であるとは思っておりません。
音楽に拘らず、クリスマスの雰囲気でワクワク上品な雰囲気であれば、
何ら問題ございません。

どうぞ宜しくお願い申し上げます。
【デザインをご考案頂きました皆様へ】

この度は、「中高年ピアノフェスティバル・チラシ」のデザインをご考案頂きまして、誠にありがとうございました。

本当に素晴らしい作品ばかりで、胸がジーンとしてまいります。

心から感謝申し上げます。

現在ご提案頂きました作品一点一点を、関係者と共に選定中でございます。

何卒宜しくお願い申し上げます。

取り急ぎ御礼まで。

日本ひだまりチェロ連盟
■ 選んだ理由

この作品は、落ち着いた赤色の中にも、華やかさがある大人のクリスマスを感じさせるデザインで、ピアノ講師陣の一番人気の作品でした。全体のイメージが何かが起こりそうな楽しい予感を感じ、文字も大変読みやすいデザインです。この様なチラシを皆様に配りすることが出来、大変嬉しく思っております。改めまして御礼申し上げます。

■ 提案者全員のお礼・コメント

この度は、「中高年ピアノフェスティバル・チラシ」のデザインをご考案下さいまして、誠にありがとうございます。デザイナー様のお一人お一人の熱い想いのこもった数々の作品に、本当に胸が一杯でございます。クリスマスのイメージはもちろんですが、60代から70代の年齢に合わせて読みやすくなさって下さったり、書体の工夫。。と細部にわたるご配慮、改めまして心より御礼申し上げます。今後もイベントに合わせてコンペ方式でデザインのご提案を依頼させて頂くことがございますので、引き続き宜しくお願い申し上げます!

```html
<!DOCTYPE html>
<html lang="ja">
<head>
<meta charset="utf-8">
<title>ひだまりチェロ・フェスティバルin岡山</title>
<link href="https://fonts.googleapis.com/css2?family=Noto+Serif+JP:wght@400;600;700;900&family=Noto+Sans+JP:wght@400;500;700&display=swap" rel="stylesheet">
<style>
:root{
  --wine:#3a0b12;
  --wine-deep:#24060b;
  --band:#1c0509;
  --red:#c8102e;
  --gold:#d8b25a;
  --gold-light:#f1dca0;
  --ink:#222;
  --line:#777;
  --green:#3a8a3a;
}
*{margin:0;padding:0;box-sizing:border-box}
html,body{width:846px;height:1200px;overflow:hidden;background:#fff}
body{font-family:"Noto Sans JP",sans-serif;color:var(--ink)}
.flyer{position:relative;width:846px;height:1200px;overflow:hidden}

.stage{position:absolute;left:0;top:0;width:846px;height:695px;
  background:radial-gradient(ellipse at 30% 40%,#5a1620 0%,var(--wine) 45%,var(--wine-deep) 100%)}
.stage-photo{position:absolute;left:0;top:250px;width:540px;height:300px;
  background:radial-gradient(ellipse at 40% 45%,rgba(230,210,190,.3) 0%,rgba(90,30,35,.45) 45%,rgba(36,6,11,0) 75%)}
.poinsettia{position:absolute;left:560px;top:488px;width:230px;height:72px;
  background:radial-gradient(ellipse at 50% 50%,#c61a22 0%,#8e1018 40%,rgba(30,80,30,.5) 65%,rgba(36,6,11,0) 80%)}

.title{position:absolute;left:30px;top:22px;font-family:"Noto Serif JP",serif;font-weight:900;color:#fff;line-height:1.15;font-size:40px;letter-spacing:1px}
.title small{font-size:30px}
.badge{position:absolute;right:26px;top:36px;width:210px;height:80px;border:2px solid var(--gold);
  color:var(--gold-light);font-family:"Noto Serif JP",serif;font-weight:700;font-size:26px;
  display:flex;align-items:center;justify-content:center;background:rgba(0,0,0,.2)}
.tagline{position:absolute;left:30px;top:130px;color:var(--gold-light);font-family:"Noto Serif JP",serif;font-size:14px}

.date{position:absolute;left:30px;top:160px;font-family:"Noto Serif JP",serif;color:var(--gold);font-weight:700;font-size:50px;letter-spacing:1px}
.date small{font-size:30px}
.venue{position:absolute;left:30px;top:232px;font-family:"Noto Serif JP",serif;color:#fff;font-size:24px;font-weight:600}
.hours{position:absolute;left:250px;top:270px;color:#fff;font-size:13px}

.divisions{position:absolute;left:540px;top:236px;width:286px;color:#fff;font-size:12px;line-height:1.55;
  border:1px solid var(--gold);background:rgba(20,3,6,.55);padding:10px 12px}
.division{margin-bottom:8px}
.division:last-child{margin-bottom:0}
.division h3{display:inline-block;background:var(--gold);color:var(--wine-deep);font-size:12px;font-weight:700;padding:1px 10px;margin-bottom:3px}
.division p{white-space:nowrap}
.division .indent{padding-left:5.5em}

.info{position:absolute;left:0;top:572px;width:846px;height:123px;background:var(--band);
  border-top:1px solid var(--gold);color:#fff;font-size:11.5px;line-height:1.6;padding:8px 30px}
.info dl{display:grid;grid-template-columns:104px 1fr;column-gap:8px}
.info dt{color:var(--gold-light)}
.info .tel{font-size:15px;font-weight:700;color:var(--gold-light)}
.info .sponsor{margin-top:4px;padding-top:3px;border-top:1px solid var(--gold);font-size:11px}

.org{position:absolute;left:0;top:695px;width:846px;height:135px;background:#fff}
.org-name{position:absolute;left:40px;top:26px;display:flex;align-items:center;gap:12px}
.org-mark{width:44px;height:44px;border-radius:50%;background:var(--green)}
.org-name .txt{font-family:"Noto Serif JP",serif;font-weight:700;font-size:28px;color:var(--green)}
.org-sub{position:absolute;left:96px;top:76px;font-size:13px;color:var(--green)}
.recruit{position:absolute;left:96px;top:96px;font-family:"Noto Serif JP",serif;font-size:22px;font-weight:700;color:var(--green)}
.notice{position:absolute;right:30px;top:24px;width:300px;border:2px solid var(--red);padding:10px 12px;font-size:12px;line-height:1.6;color:var(--red)}

.form{position:absolute;left:30px;top:840px;width:786px}
.form-head{display:flex;justify-content:space-between;align-items:flex-end;border-bottom:2px solid var(--ink);padding-bottom:4px;margin-bottom:8px}
.form-head h2{font-size:18px;font-weight:700}
.form-head span{font-size:11px}
.form table{width:100%;border-collapse:collapse;font-size:11px;table-layout:fixed}
.form td{border:1px solid var(--line);padding:5px 6px;height:44px;vertical-align:top;white-space:nowrap;overflow:hidden}
.form td.label{background:#f4f4f4}
.form tr.note td{height:70px}
</style>
</head>
<body>
<div class="flyer">
  <section class="stage">
    <div class="stage-photo" role="img" aria-label="暗がりに照らされた演奏用楽器の写真"></div>
    <div class="poinsettia" role="img" aria-label="赤いポインセチアの飾り"></div>

    <h1 class="title">ひだまりチェロ・<br>フェスティバル<small>in</small>岡山</h1>
    <div class="badge">1分15秒の花舞台</div>
    <p class="tagline">「ここまで弾けた!」その喜びを1分15秒に込めて…特別な舞台でチャレンジしてみませんか?</p>

    <p class="date">2015年12月1日<small>(火)</small></p>
    <p class="venue">岡山みなと会館 ひびきホール</p>
    <p class="hours">開場11:30 開演12:00</p>

    <div class="divisions">
      <div class="division">
        <h3>グレード認定 部門</h3>
        <p>【初級】1部門 5,940円(税込)<br>【中級】2部門 6,480円(税込)<br>【上級】3部門 7,020円(税込)</p>
      </div>
      <div class="division">
        <h3>自由曲演奏部門</h3>
        <p>【演奏時間】1分15秒以内<br>【参加費】5,400円(税込)</p>
      </div>
      <div class="division">
        <h3>グループ演奏部門</h3>
        <p>【演奏時間】2名で演奏 2分15秒以内<br><span class="indent">3名以上で演奏 3分15秒以内</span><br>【参加費】お一人様 3,780円(税込)</p>
      </div>
    </div>

    <div class="info">
      <dl>
        <dt>■ お申込み方法</dt><dd>下記の参加申込書にご記入の上、FAXまたはご郵送にてお申込みください。</dd>
        <dt>■ お問い合わせ</dt><dd>〒700-0000 岡山県岡山市北区さくら町1-2-3 ひかりビル2F 日本ひだまりチェロ連盟 さくら町事務所</dd>
        <dt></dt><dd><span class="tel">TEL 086-555-0142 / FAX 086-555-0143</span>  E-mail info@hidamari-cello.example</dd>
      </dl>
      <p class="sponsor">■ 主催:日本ひだまりチェロ連盟 ■ 後援:はれのくに音楽文化振興会・みなと町芸術交流ネット・地元新聞社・地元放送局</p>
    </div>
  </section>

  <section class="org">
    <div class="org-name"><span class="org-mark"></span><span class="txt">日本ひだまりチェロ連盟</span></div>
    <p class="org-sub">「笑顔・喜び・憩い」の音楽を!</p>
    <p class="recruit">趣味で楽しみたい演奏者大募集</p>
    <div class="notice">お申込・お問合せはお近くの事務所まで。当日の見学も受け付けております。お気軽にご連絡ください。</div>
  </section>

  <section class="form">
    <div class="form-head"><h2>参加申込書/10月2日(金)締切</h2><span>ご記入いただいた個人情報は本催事のみに使用します。</span></div>
    <table>
      <colgroup><col style="width:86px"><col style="width:200px"><col style="width:86px"><col style="width:180px"><col style="width:86px"><col></colgroup>
      <tr><td class="label">ふりがな<br>お名前</td><td></td><td class="label">ご住所</td><td colspan="3">〒</td></tr>
      <tr><td class="label">電話番号</td><td></td><td class="label">年齢</td><td colspan="3"></td></tr>
      <tr><td class="label">曲目</td><td></td><td class="label">作曲者名</td><td></td><td class="label">演奏時間</td><td>分 秒</td></tr>
      <tr><td class="label">参加部門</td><td>□ グレード認定部門<br>□ 自由曲演奏部門</td><td colspan="2">□ グループ演奏部門</td><td class="label">チェロ経験</td><td>年</td></tr>
      <tr class="note"><td class="label">備考</td><td colspan="5"></td></tr>
    </table>
  </section>
</div>
</body>
</html>
```